Stationary design for real estate company in Trinidad and Tobago

Kestra Realty Ltd. , real estate company operating in Trinidad and Tobago, requires a sleek, modern and professional stationary package to wow our customers and potential new clients. we want to look sleek and professional; first impressions count in this business!
Business Address:
Level 1, Marlowe Point Tower
4C Seldon Grove Boulevard
Marlowe Point
Colwyn Pereira Highway
Port of Spain
Trinidad
Tel: + 1 868 555 0147
www.kestra-tt.com
info@kestra-tt.com

```html
<!DOCTYPE html>
<html lang="en">
<head>
<meta charset="utf-8">
<title>Kestra Realty – Business Card</title>
<link href="https://fonts.googleapis.com/css2?family=Montserrat:wght@400;500;700&display=swap" rel="stylesheet">
<style>
  :root {
    --navy: #15315c;
    --gold: #bf9f62;
    --white: #ffffff;
    --ink: #1d1d22;
    --page: #e9eaec;
  }
  * { margin: 0; padding: 0; box-sizing: border-box; }
  html, body { width: 1200px; height: 1200px; overflow: hidden; }
  body {
    background: var(--page);
    font-family: "Montserrat", sans-serif;
    display: flex;
    flex-direction: column;
    align-items: center;
    justify-content: center;
    gap: 60px;
  }
  .card {
    position: relative;
    width: 760px;
    height: 434px;
    border-radius: 28px;
    overflow: hidden;
    box-shadow: 0 10px 30px rgba(0,0,0,0.15);
  }
  /* Front */
  .card-front { background: var(--white); }
  .card-front .brand {
    position: absolute;
    top: 64px;
    right: 70px;
    display: flex;
    align-items: center;
    gap: 16px;
  }
  .brand-dot {
    width: 54px; height: 54px;
    border-radius: 50%;
    background: var(--gold);
  }
  .brand-name {
    font-weight: 500;
    font-size: 46px;
    letter-spacing: 2px;
    text-transform: uppercase;
    line-height: 1;
  }
  .card-front .brand-name { color: var(--navy); }
  .contact {
    position: absolute;
    left: 64px;
    top: 150px;
    color: var(--ink);
  }
  .person-name {
    color: var(--navy);
    font-weight: 700;
    font-size: 30px;
    letter-spacing: 0.5px;
    line-height: 1.05;
  }
  .person-title {
    font-size: 15px;
    letter-spacing: 1px;
    margin-bottom: 12px;
  }
  .contact-list { list-style: none; }
  .contact-list li {
    display: flex;
    align-items: center;
    gap: 12px;
    font-size: 19px;
    line-height: 1.5;
  }
  .contact-list svg { width: 20px; height: 20px; fill: var(--navy); flex: none; }
  .address {
    position: absolute;
    right: 60px;
    bottom: 56px;
    text-align: right;
    color: var(--navy);
    font-size: 15px;
    line-height: 1.4;
  }
  .bottom-band {
    position: absolute;
    left: 0; right: 0; bottom: 0;
    height: 32px;
    background: var(--navy);
    border-top: 5px solid var(--gold);
  }
  /* Back */
  .card-back {
    background: var(--navy);
    display: flex;
    align-items: center;
    justify-content: center;
  }
  .card-back .brand { display: flex; align-items: center; gap: 22px; }
  .card-back .brand-dot { width: 84px; height: 84px; }
  .card-back .brand-name { color: var(--white); font-size: 62px; }
</style>
</head>
<body>
  <section class="card card-front">
    <div class="brand">
      <span class="brand-dot"></span>
      <span class="brand-name">Kestra Realty</span>
    </div>
    <div class="contact">
      <p class="person-name">FULL NAME</p>
      <p class="person-title">TITLE</p>
      <ul class="contact-list">
        <li>
          <svg viewBox="0 0 24 24" aria-hidden="true"><path d="M6.6 10.8a15.1 15.1 0 0 0 6.6 6.6l2.2-2.2a1 1 0 0 1 1-.25 11.4 11.4 0 0 0 3.6.57 1 1 0 0 1 1 1V20a1 1 0 0 1-1 1A17 17 0 0 1 3 4a1 1 0 0 1 1-1h3.5a1 1 0 0 1 1 1c0 1.25.2 2.46.57 3.6a1 1 0 0 1-.25 1z"/></svg>
          + 1 868 555 0147
        </li>
        <li>
          <svg viewBox="0 0 24 24" aria-hidden="true"><path d="M12 2a10 10 0 1 0 0 20 10 10 0 0 0 0-20zm6.9 6h-2.9a15.6 15.6 0 0 0-1.4-3.6A8 8 0 0 1 18.9 8zM12 4c.8 1.2 1.5 2.5 1.9 4h-3.8c.4-1.5 1.1-2.8 1.9-4zM4.3 14a8.2 8.2 0 0 1 0-4h3.4a16.5 16.5 0 0 0 0 4zm.8 2h2.9c.3 1.300.8 2.5 1.4 3.6A8 8 0 0 1 5.1 16zM8 8H5.1a8 8 0 0 1 4.3-3.6C8.8 5.5 8.3 6.7 8 8zm4 12c-.8-1.2-1.5-2.5-1.900-4h3.8c-.4 1.5-1.100 2.8-1.900 4zm2.3-6H9.7a14.7 14.7 0 0 1 0-4h4.6a14.7 14.7 0 0 1 0 4zm.3 5.6c.6-1.100 1.100-2.300 1.400-3.600h2.900a8 8 0 0 1-4.300 3.600zm1.700-5.600a16.5 16.5 0 0 0 0-4h3.400a8.200 8.200 0 0 1 0 4z"/></svg>
          www.kestra-tt.com
        </li>
        <li>
          <svg viewBox="0 0 24 24" aria-hidden="true"><path d="M2 5h20v14H2zm2 2v.5l8 5 8-5V7zm0 2.8V17h16V9.8l-8 5z"/></svg>
          info@kestra-tt.com
        </li>
      </ul>
    </div>
    <p class="address">
      Level 1, Marlowe Point Tower 4C Seldon Grove Boulevard<br>
      Marlowe Point, Colwyn Pereira Highway, Port of Spain Trinidad
    </p>
    <div class="bottom-band"></div>
  </section>

  <section class="card card-back">
    <div class="brand">
      <span class="brand-dot"></span>
      <span class="brand-name">Kestra Realty</span>
    </div>
  </section>
</body>
</html>
```